Prairie Run and Pointing Dog kennel

Need Price packages outlined for the bird hunting business. List the kennel and that we provide training and dogs for sale.
The preserve is "Tall Heron Expeditions" the dog kennel is "Pine Hollow Setters"
1/2 Day Upland Field Hunts: 5 Pheasants $120
7 Chukar $125
Continental Hunt 12 Pheasants $325 includes meal, minimum 12 hunters
Guides available $100

Target Market(s)

upland bird hunters

Industry/Entity Type

hunting, outdoor

Colors
EE7325
F08F49
F5BC92
FAE3D3
FDF4ED

```html
<!DOCTYPE html>
<html lang="en">
<head>
<meta charset="utf-8">
<title>Tall Heron Expeditions – Upland Hunts Flyer</title>
<link rel="stylesheet" href="https://fonts.googleapis.com/css2?family=Abril+Fatface&family=Crimson+Text:wght@700&family=Oswald:wght@600&family=Poppins:wght@400;500;600;700&family=Staatliches&display=swap">
<style>
  :root {
    --backdrop: #b3b3b3;
    --sky: #8a4413;
    --plank: #b06a22;
    --plank-edge: #8c4f16;
    --ink: #000000;
    --gold: #f0a850;
    --cream: #fdf4ed;
    --price-bg: #9a5a1e;
    --price-edge: #c07a32;
    --rule: #5a5a5a;
  }
  * { box-sizing: border-box; margin: 0; padding: 0; }
  html, body { width: 1064px; height: 1200px; overflow: hidden; }
  body { background: var(--backdrop); font-family: "Poppins", sans-serif; }

  .flyer {
    position: absolute; left: 68px; top: 0;
    width: 927px; height: 1200px;
    background: var(--sky);
    overflow: hidden;
    color: var(--cream);
  }
  .abs { position: absolute; }

  .title {
    left: 0; width: 100%; text-align: center;
    font-family: "Abril Fatface", serif; font-size: 70px; line-height: 1;
    color: var(--cream); text-shadow: 3px 2px 0 var(--gold);
    letter-spacing: -1px;
  }
  .title--one { top: 50px; }
  .title--two { top: 122px; }

  .plank {
    left: 192px; top: 205px; width: 544px; height: 94px;
    background: linear-gradient(180deg, var(--plank) 0%, var(--plank-edge) 100%);
    border-radius: 4px;
  }
  .plank-text {
    left: 192px; top: 212px; width: 544px; text-align: center;
    font-family: "Staatliches", sans-serif; color: var(--cream);
    line-height: 1.1;
  }
  .plank-text .city { font-size: 38px; display: block; }
  .plank-text .licence { font-size: 40px; display: block; letter-spacing: 1px; }

  .scene {
    left: 0; top: 330px; width: 100%; height: 640px;
    background: linear-gradient(180deg, rgba(0,0,0,0) 0%, rgba(60,28,6,0.35) 45%, rgba(25,10,2,0.85) 85%, var(--ink) 100%);
  }
  .lower { left: 0; top: 960px; width: 100%; height: 240px; background: var(--ink); }
  .lower-band { left: 0; top: 830px; width: 100%; height: 140px; background: var(--ink); }

  .preserve-mark {
    left: 313px; top: 330px; width: 300px; height: 120px;
    display: flex; flex-direction: column; align-items: center; justify-content: center; gap: 10px;
  }
  .preserve-mark .dot { width: 56px; height: 56px; border: 3px solid var(--cream); border-radius: 50%; }
  .preserve-mark .name { font-family: "Poppins", sans-serif; font-weight: 700; font-size: 28px; line-height: 1; color: var(--cream); }

  .field-heading {
    left: 0; width: 100%; top: 470px; text-align: center;
    font-family: "Crimson Text", serif; font-weight: 700; font-size: 44px; color: var(--gold); line-height: 1;
  }
  .package { width: 200px; text-align: center; }
  .package .bird { font-weight: 700; font-size: 26px; line-height: 1; }
  .package .price {
    display: inline-block; margin-top: 13px; width: 107px; height: 45px;
    background: var(--price-bg); border: 2px solid var(--price-edge);
    font-weight: 600; font-size: 36px; line-height: 42px; color: var(--cream);
  }
  .price sup, .guide sup, .list sup { font-size: 0.5em; vertical-align: 0.8em; }
  .package--pheasant { left: 195px; top: 524px; }
  .package--chukar { left: 398px; top: 524px; }
  .package--quail { left: 567px; top: 524px; }

  .guide {
    left: 0; width: 100%; top: 645px; text-align: center;
    font-weight: 700; font-size: 31px; line-height: 1.1; color: var(--gold);
  }
  .guide .amount { color: var(--cream); }

  .section-title { font-weight: 700; font-size: 21px; color: var(--gold); line-height: 1; }
  .list { list-style: none; font-size: 15px; line-height: 1.15; color: var(--cream); }
  .list li { position: absolute; left: 0; padding-left: 26px; width: 100%; }
  .list svg { position: absolute; left: 0; top: 1px; width: 15px; height: 15px; }
  .list b { font-weight: 700; }

  .col-left { left: 58px; top: 903px; width: 380px; }
  .col-right { left: 509px; top: 903px; width: 390px; }
  .col-rule { left: 464px; top: 905px; width: 1px; height: 150px; background: var(--rule); }

  .kennel-note {
    left: 49px; top: 1112px;
    font-family: "Oswald", sans-serif; font-weight: 600; font-size: 17px; line-height: 1.4;
    text-transform: uppercase; letter-spacing: -0.3px; transform: scaleX(0.92); transform-origin: left;
  }
  .footer-rule { left: 347px; top: 1109px; width: 1px; height: 44px; background: var(--rule); }
  .contact { left: 377px; top: 1104px; }
  .contact .person { font-weight: 500; font-size: 21px; color: var(--gold); line-height: 1.1; }
  .contact .phone { font-weight: 700; font-size: 24px; line-height: 1.2; display: flex; align-items: center; gap: 6px; }
  .contact .phone svg { width: 12px; height: 12px; }

  .partner {
    font-family: "Poppins", sans-serif; font-weight: 500; color: var(--cream);
    text-align: center; line-height: 1.15;
  }
  .partner--kennel { left: 584px; top: 1100px; width: 174px; font-size: 16px; }
  .partner--preserve { left: 785px; top: 1100px; width: 110px; font-size: 14px; }
</style>
</head>
<body>
<main class="flyer">
  <div class="abs scene" role="img" aria-label="Silhouettes of flying quail, pine trees, a hunter aiming a shotgun and a pointing dog on a hill at dusk"></div>
  <div class="abs lower-band"></div>
  <div class="abs lower"></div>

  <h1>
    <span class="abs title title--one">TALL HERON</span>
    <span class="abs title title--two">EXPEDITIONS LLC</span>
  </h1>

  <div class="abs plank" role="img" aria-label="Weathered wooden sign board"></div>
  <p class="abs plank-text">
    <span class="city">Millbrook, MO</span>
    <span class="licence">Licensed Shooting Preserve</span>
  </p>

  <div class="abs preserve-mark">
    <span class="dot"></span>
    <span class="name">Prairie Run</span>
  </div>

  <h2 class="abs field-heading">Upland Field Hunts - ½ Day</h2>

  <div class="abs package package--pheasant"><div class="bird">5 Pheasants</div><div class="price"><sup>$</sup>120</div></div>
  <div class="abs package package--chukar"><div class="bird">7 Chukar</div><div class="price"><sup>$</sup>125</div></div>
  <div class="abs package package--quail"><div class="bird">8 Quail</div><div class="price"><sup>$</sup>100</div></div>

  <p class="abs guide">GUIDE AVAILABLE<br><span class="amount"><sup>$</sup>100</span> PER HALF DAY</p>

  <section class="abs col-left">
    <h3 class="section-title">CONTINENTAL PHEASANT HUNT</h3>
    <ul class="list">
      <li style="top:28px"><svg viewBox="0 0 16 16"><circle cx="8" cy="8" r="6.5" fill="none" stroke="#f0a850" stroke-width="1.5"/><path d="M5 8.2l2 2 4.5-4.8" fill="none" stroke="#f0a850" stroke-width="1.8"/></svg><b>12</b> Hunter Minimum</li>
      <li style="top:56px"><svg viewBox="0 0 16 16"><circle cx="8" cy="8" r="6.5" fill="none" stroke="#f0a850" stroke-width="1.5"/><path d="M5 8.2l2 2 4.5-4.8" fill="none" stroke="#f0a850" stroke-width="1.8"/></svg><b><sup>$</sup>325</b> per hunter, includes 12 Pheasants<br>per hunter &amp; meal.</li>
      <li style="top:101px"><svg viewBox="0 0 16 16"><circle cx="8" cy="8" r="6.5" fill="none" stroke="#f0a850" stroke-width="1.5"/><path d="M5 8.2l2 2 4.5-4.8" fill="none" stroke="#f0a850" stroke-width="1.8"/></svg>All hunts include bird cleaning</li>
      <li style="top:131px"><svg viewBox="0 0 16 16"><circle cx="8" cy="8" r="6.5" fill="none" stroke="#f0a850" stroke-width="1.5"/><path d="M5 8.2l2 2 4.5-4.8" fill="none" stroke="#f0a850" stroke-width="1.8"/></svg>Lodging available, call for pricing</li>
    </ul>
  </section>

  <div class="abs col-rule"></div>

  <section class="abs col-right">
    <h3 class="section-title">GUIDED SPRING TURKEY HUNTS</h3>
    <ul class="list">
      <li style="top:28px"><svg viewBox="0 0 16 16"><circle cx="8" cy="8" r="6.5" fill="none" stroke="#f0a850" stroke-width="1.5"/><path d="M5 8.2l2 2 4.5-4.8" fill="none" stroke="#f0a850" stroke-width="1.8"/></svg><b>3 Day</b> Hunt includes meals &amp; lodging <b><sup>$</sup>1600</b></li>
      <li style="top:60px"><svg viewBox="0 0 16 16"><circle cx="8" cy="8" r="6.5" fill="none" stroke="#f0a850" stroke-width="1.5"/><path d="M5 8.2l2 2 4.5-4.8" fill="none" stroke="#f0a850" stroke-width="1.8"/></svg>Guided Whitetail Deer Hunts -Rifle &amp; Archery</li>
      <li style="top:92px"><svg viewBox="0 0 16 16"><circle cx="8" cy="8" r="6.5" fill="none" stroke="#f0a850" stroke-width="1.5"/><path d="M5 8.2l2 2 4.5-4.8" fill="none" stroke="#f0a850" stroke-width="1.8"/></svg><b>5 Day</b> Hunt includes meals &amp; lodging <b><sup>$</sup>2750</b></li>
    </ul>
  </section>

  <p class="abs kennel-note">We provide training and dogs for sale.<br>Puppies and started dogs available!</p>

  <div class="abs footer-rule"></div>

  <div class="abs contact">
    <div class="person">Dale Morgan</div>
    <div class="phone"><svg viewBox="0 0 12 12"><circle cx="6" cy="6" r="5.5" fill="#f0a850"/><path d="M4 3.2l1 1.3-.6.8c.4.9 1 1.5 1.9 1.9l.8-.6 1.3 1-.6 1.1c-2.4-.3-4.3-2.2-4.6-4.6z" fill="#000"/></svg>555-014-2288</div>
  </div>

  <p class="abs partner partner--kennel">Pine Hollow Setters<br>Cedar Falls, MO</p>
  <p class="abs partner partner--preserve">Tall Heron<br>Expeditions</p>
</main>
</body>
</html>
```